Harlow Stonefield Civil Construction website design

We want a Bold website to promote our Heavy Civil Construction company, We would like an organic / tangible feel to the site. The pictures will be over saturated so they pop. We need to be able to easliy upload new projects and pictures on a regular basis.
Home page will have a full screen width image, "home page image" with silhouette and logo. It will also have about us area and picture
Page 2 will be Project Gallery with pictures in project folders
Page 3 will be an employment application form and submission
Page 4 will be Contact Us
Target Market(s)
Construction indusrty
Industry/Entity Type
Contractor
Coding
Coded - Design and coding required
Number of Pages Required
4 page
Font styles to use
Other font styles liked:
- Hypatia Sans Pro Light
Look and feel

```html
<!DOCTYPE html>
<html lang="en">
<head>
<meta charset="utf-8">
<title>Harlow Stonefield Civil Construction</title>
<link href="https://fonts.googleapis.com/css2?family=Fira+Sans:wght@500;600;700&family=Roboto+Condensed:ital,wght@0,400;0,700;1,400&family=Montserrat:wght@400;500&display=swap" rel="stylesheet">
<style>
:root{
  --blue:#2b3f9b;
  --blue-deep:#22348a;
  --ink:#222;
  --text:#444;
  --muted:#777;
  --nav:#1e1e1e;
  --light:#f4f4f6;
  --band:#d9d9db;
  --white:#fff;
  --dark:#3a3a3d;
}
*{box-sizing:border-box;margin:0;padding:0}
html,body{width:1200px;height:3238px;overflow:hidden}
body{position:relative;background:var(--white);font-family:"Roboto Condensed",sans-serif;color:var(--text)}
.abs{position:absolute}
a{color:inherit;text-decoration:none}

/* header */
.brand{left:155px;top:16px;display:flex;align-items:center;gap:10px}
.brand-mark{width:36px;height:36px;border:3px solid var(--blue);border-radius:4px}
.brand-name{font-family:"Montserrat",sans-serif;color:var(--blue);font-size:17px;line-height:1.05;font-weight:500}
.brand-name small{display:block;font-size:10px;letter-spacing:3.2px;color:var(--blue)}
.contact-top{top:20px;display:flex;gap:10px;align-items:center}
.contact-top .t1{font-size:11px;color:var(--ink);font-weight:700}
.contact-top .t2{font-size:15px;color:var(--blue);font-weight:700}
.clock{width:34px;height:34px}
.divider{left:897px;top:20px;width:1px;height:38px;background:#ccc}

/* nav */
.nav-blue{left:0;top:77px;width:1200px;height:40px}
.menu{left:155px;top:77px;height:36px;display:flex;align-items:center;color:#fff;font-size:13px;font-weight:700}
.menu span.sep{margin:0 20px;color:#aaa;font-weight:400}
.search{left:818px;top:84px;width:226px;height:25px;background:var(--blue-deep);border:1px solid #7a86c8;color:#d6dbf3;font-size:11px;padding:6px 10px}
.search-btn{left:1017px;top:85px;width:26px;height:23px;background:#111}

/* hero */
.hero{left:0;top:117px;width:1200px;height:508px}
.hero-title{left:155px;top:280px;font-family:"Fira Sans",sans-serif;font-weight:700;font-size:36px;color:#fff;letter-spacing:.5px;white-space:nowrap}
.hero-text{left:155px;top:338px;width:340px;color:#fff;font-size:14.5px;font-weight:700;line-height:29px}
.btn{display:flex;align-items:center;justify-content:space-between;border-radius:24px;font-family:"Roboto Condensed",sans-serif;font-weight:700;color:var(--blue);font-size:17px}
.btn .arrow{width:31px;height:31px;border-radius:50%;background:var(--blue);display:flex;align-items:center;justify-content:center}
.btn-white{background:#fff;padding:0 5px 0 14px}
.btn-outline{border:2.5px solid var(--blue);background:#fff;padding:0 5px 0 18px}

/* newsletter */
.news{left:0;top:625px;width:1200px;height:132px}
.call-label{left:155px;top:668px;font-size:13px;font-weight:700;color:var(--ink)}
.call-num{left:155px;top:690px;font-size:17px;font-weight:700;color:var(--blue);letter-spacing:.5px}
.news-title{left:377px;top:655px;font-family:"Fira Sans",sans-serif;font-weight:600;font-size:17px;color:var(--ink)}
.field{height:42px;background:#fff;font-size:11px;color:#333;padding:14px 16px}

/* about */
.about-rule{left:533px;top:888px;width:52px;height:4px;background:var(--blue)}
.about-title{left:606px;top:870px;width:440px;font-family:"Fira Sans",sans-serif;font-weight:600;font-size:29px;line-height:38px;color:var(--ink)}
.about-text{left:606px;top:964px;width:440px;font-size:13.3px;line-height:28px;color:var(--text)}
.about-text p+p{margin-top:13px}

/* testimonials */
.testi{left:0;top:1339px;width:1200px;height:437px;background:linear-gradient(180deg,#eeeef0,#e6e6e9)}
.quote{left:340px;top:1588px;width:520px;text-align:center;font-style:italic;font-size:13.5px;line-height:23px;color:#555}
.quote-icon{left:584px;top:1654px;width:31px;height:31px;border-radius:50%;background:var(--blue);color:#fff;font-family:"Fira Sans",sans-serif;font-weight:700;font-size:18px;text-align:center;line-height:34px}
.quote-name{left:500px;top:1697px;width:200px;text-align:center;font-size:18px;font-weight:700;color:#333}

/* gallery */
.section-title{left:400px;top:1855px;width:400px;text-align:center;font-family:"Fira Sans",sans-serif;font-weight:600;font-size:29px;color:var(--ink)}
.title-rule{left:573px;top:1905px;width:42px;height:3px;background:var(--blue)}
.ph{position:absolute}

/* cta */
.cta{left:0;top:2512px;width:1200px;height:400px;background:linear-gradient(180deg,#38383b,#2c2c2e)}
.cta-title{left:370px;top:2562px;width:460px;text-align:center;font-family:"Fira Sans",sans-serif;font-weight:600;font-size:29px;line-height:44px;color:#fff}
.cta-sub{left:300px;top:2666px;width:600px;text-align:center;color:#fff;font-size:15px;font-weight:700}

/* footer */
.foot-about{left:154px;top:3005px;width:268px;font-size:13.3px;line-height:28px;color:#444}
.foot-h{font-family:"Fira Sans",sans-serif;font-weight:600;font-size:16px;color:var(--ink)}
.foot-list{font-size:13.3px;color:#444;list-style:none}
.foot-list li{display:flex;align-items:flex-start;gap:10px}
.ico{width:14px;height:14px;flex:none;margin-top:3px}
.soc-dot{width:12px;height:12px;border-radius:50%;background:#222;flex:none;margin-top:4px}
.foot-rule{left:155px;top:3169px;width:890px;height:1px;background:#bbb}
.copy{left:400px;top:3197px;width:400px;text-align:center;font-size:11.5px;color:#333}
</style>
</head>
<body>

<!-- Header -->
<div class="abs brand">
  <div class="brand-mark"></div>
  <div class="brand-name">HARLOW STONEFIELD<small>CIVIL CONSTRUCTION</small></div>
</div>
<div class="abs contact-top" style="left:690px">
  <svg class="clock" viewBox="0 0 34 34"><path d="M30 17A13 13 0 1 1 24 6" fill="none" stroke="#111" stroke-width="2.5"/><path d="M22 2l4 4-5 2" fill="none" stroke="#111" stroke-width="2.5"/><text x="17" y="21" font-size="9" text-anchor="middle" font-family="Roboto Condensed" fill="#111">24/7</text></svg>
  <div><div class="t1">It's 07:00 am &amp; We're Open</div><div class="t2">EMERGENCY SERVICE</div></div>
</div>
<div class="abs divider"></div>
<div class="abs contact-top" style="left:918px">
  <div><div class="t1">Call Us Today!</div><div class="t2">(+1) 555 010 2040</div></div>
</div>

<!-- Navigation -->
<svg class="abs nav-blue" viewBox="0 0 1200 40" width="1200" height="40">
  <rect width="1200" height="36" fill="#1e1e1e"/>
  <polygon points="806,0 1200,0 1200,36 786,36" fill="#2b3f9b"/>
  <polygon points="796,0 802,0 782,36 776,36" fill="#fff"/>
  <rect y="36" width="1200" height="4" fill="#2b3f9b"/>
</svg>
<nav class="abs menu">
  <a>HOME</a><span class="sep">|</span><a>ABOUT US</a><span class="sep">|</span><a>PROJECT GALLERY</a><span class="sep">|</span><a>EMPLOYEE APPLICATION</a><span class="sep">|</span><a>CONTACT US</a>
</nav>
<div class="abs search">Search For Site....</div>
<div class="abs search-btn"><svg width="26" height="23" viewBox="0 0 26 23"><circle cx="12" cy="10" r="4.5" fill="none" stroke="#fff" stroke-width="2"/><path d="M15 13l4 4" stroke="#fff" stroke-width="2"/></svg></div>

<!-- Hero -->
<svg class="abs hero" viewBox="0 0 1200 508" width="1200" height="508">
  <defs>
    <linearGradient id="heroPh" x1="0" y1="0" x2="0" y2="1">
      <stop offset="0" stop-color="#7da3d6"/><stop offset=".3" stop-color="#3f6a2e"/><stop offset=".6" stop-color="#8c8a7c"/><stop offset="1" stop-color="#6b5a3e"/>
    </linearGradient>
    <linearGradient id="heroBlue" x1="0" y1="0" x2="1" y2="0">
      <stop offset="0" stop-color="#2a3ea0" stop-opacity=".95"/><stop offset="1" stop-color="#2f44a8" stop-opacity=".9"/>
    </linearGradient>
  </defs>
  <rect width="1200" height="508" fill="url(#heroPh)" role="img" aria-label="Photo of an excavator and crew building a gabion retaining wall"/>
  <polygon points="0,0 477,0 597,508 0,508" fill="url(#heroBlue)"/>
  <circle cx="79" cy="234" r="15" fill="#8593cf"/>
  <path d="M86 234H72M78 227l-7 7 7 7" stroke="#2a3ea0" stroke-width="3" fill="none"/>
  <circle cx="1120" cy="234" r="15" fill="#fff" fill-opacity=".3"/>
  <path d="M1113 234h14M1121 227l7 7-7 7" stroke="#6b6b6b" stroke-width="3" fill="none"/>
</svg>
<h1 class="abs hero-title">HARLOW STONEFIELD</h1>
<p class="abs hero-text">Nemo enim ipsam voluptatem quia voluptas sitouats pernatur autaut, sequia conseuntur nesutas.</p>
<a class="abs btn btn-white" style="left:155px;top:415px;width:151px;height:43px">Get In Touch <span class="arrow"><svg width="16" height="10" viewBox="0 0 16 10"><path d="M1 5h13M10 1l4 4-4 4" stroke="#fff" stroke-width="2" fill="none"/></svg></span></a>

<!-- Newsletter -->
<svg class="abs news" viewBox="0 0 1200 132" width="1200" height="132">
  <rect width="1200" height="132" fill="#d9d9db"/>
  <polygon points="0,0 310,0 348,66 310,132 0,132" fill="#cacacc"/>
  <polygon points="310,0 318,0 356,66 318,132 310,132 348,66" fill="#e6e6e8"/>
</svg>
<div class="abs call-label">CALL US TODAY!</div>
<div class="abs call-num">(+1) 555 010 2040</div>
<h2 class="abs news-title">SUBSCRIBE NEWSLETTER!</h2>
<div class="abs field" style="left:378px;top:686px;width:237px">Full Name:</div>
<div class="abs field" style="left:637px;top:686px;width:237px">Email Address:</div>
<a class="abs btn btn-white" style="left:894px;top:687px;width:151px;height:42px">Get In Touch <span class="arrow"><svg width="16" height="10" viewBox="0 0 16 10"><path d="M1 5h13M10 1l4 4-4 4" stroke="#fff" stroke-width="2" fill="none"/></svg></span></a>

<!-- About -->
<svg class="abs" style="left:0;top:780px" width="580" height="520" viewBox="0 0 580 520">
  <polygon points="42,15 62,4 62,-7 42,-18 22,-7 22,4" transform="translate(0,28)" fill="#e2e2e4"/>
  <polygon points="144,35 244,92 244,208 144,265 44,208 44,92" fill="#ececee"/>
  <polygon points="144,280 244,337 244,453 144,510 44,453 44,337" fill="none" stroke="#e6e6e8" stroke-width="2"/>
  <polygon points="335,25 385,54 385,112 335,141 285,112 285,54" fill="none" stroke="#e6e6e8" stroke-width="2"/>
  <polygon points="500,115 520,127 520,150 500,162 480,150 480,127" fill="#e6e6e8"/>
  <polygon points="460,350 545,398 545,496 460,544" fill="#ececee"/>
  <polygon points="460,440 480,452 480,475 460,487 440,475 440,452" fill="#e0e0e2"/>
  <polygon points="334,80 510,180 510,380 334,480 156,380 156,180" fill="#8c8c8c"/>
  <defs><linearGradient id="aboutPh" x1="0" y1="0" x2="0" y2="1"><stop offset="0" stop-color="#5f8fd6"/><stop offset=".45" stop-color="#d7b23a"/><stop offset=".75" stop-color="#4a6b3a"/><stop offset="1" stop-color="#6a5034"/></linearGradient></defs>
  <polygon points="334,84 506,182 506,378 334,476 160,378 160,182" fill="url(#aboutPh)" role="img" aria-label="Photo of a yellow excavator on a site under blue sky"/>
</svg>
<div class="abs about-rule"></div>
<h2 class="abs about-title">Nemo enim ipsam voluptatem quia voluptas sit asper</h2>
<div class="abs about-text">
  <p>Sed ut perspiciatis unde omnis iste natusauror&nbsp; sit voluptatem accusantium doloremque laudantium, totam rem aperiam, eaque ipsa quae ab illo inventore veritatis et quasi architecto beatae vitae dicta sunt explicabo. Nemo enim ipsam voluptatem quia voluptas sit aspernatur autodit fugit, sed quia.</p>
  <p>Sed ut perspiciatis unde omnis iste natusauror sit voluptatem accusantium doloremque laudantium, totam rem aperiam, eaque ipsa quae ab illo inventore veritatis et quasi architecto beatae vitae dicta sunt explicabo.</p>
</div>
<a class="abs btn btn-outline" style="left:602px;top:1193px;width:154px;height:47px">Learn More <span class="arrow"><svg width="16" height="10" viewBox="0 0 16 10"><path d="M1 5h13M10 1l4 4-4 4" stroke="#fff" stroke-width="2" fill="none"/></svg></span></a>

<!-- Testimonials -->
<div class="abs testi"></div>
<svg class="abs" style="left:0;top:1339px" width="1200" height="300" viewBox="0 0 1200 300">
  <circle cx="118" cy="145" r="10" fill="#777"/><path d="M123 145h-9M118 140l-5 5 5 5" stroke="#fff" stroke-width="2" fill="none"/>
  <circle cx="1085" cy="145" r="10" fill="#777"/><path d="M1080 145h9M1085 140l5 5-5 5" stroke="#fff" stroke-width="2" fill="none"/>
  <polygon points="253,104 298,124 298,166 253,186 208,166 208,124" fill="#a3a6ab" role="img" aria-label="Client portrait"/>
  <polygon points="408,104 453,124 453,166 408,186 363,166 363,124" fill="#a89a8c" role="img" aria-label="Client portrait"/>
  <polygon points="600,63 693,107 693,186 600,230 507,186 507,107" fill="none" stroke="#2b3f9b" stroke-width="3"/>
  <polygon points="600,72 684,112 684,181 600,221 516,181 516,112" fill="none" stroke="#2b3f9b" stroke-width="2"/>
  <polygon points="600,80 676,116 676,177 600,213 524,177 524,116" fill="#c9b898" role="img" aria-label="Featured client portrait"/>
  <polygon points="790,104 835,124 835,166 790,186 745,166 745,124" fill="#d8c2b0" role="img" aria-label="Client portrait"/>
  <polygon points="945,104 990,124 990,166 945,186 900,166 900,124" fill="#4e5460" role="img" aria-label="Client portrait"/>
</svg>
<p class="abs quote">“ Nemo enim ipsam voluptatem quia voluptas sit aspernatur aut odit aut fugit, sed quia conset quuntur magni dolores eos qui ratione voluptatem sequi nesciunt. ”</p>
<div class="abs quote-icon">”</div>
<div class="abs quote-name">Mark Ellison</div>

<!-- Gallery -->
<h2 class="abs section-title">Photo Gallery</h2>
<div class="abs title-rule"></div>
<div class="ph" style="left:156px;top:1942px;width:537px;height:481px;background:linear-gradient(180deg,#3d6fc2 0%,#6b7a86 40%,#9aa0a0 70%,#e7e9ec 100%)" role="img" aria-label="Photo of steel pipe rack structure with erosion mat installation"></div>
<div class="ph" style="left:701px;top:1942px;width:168px;height:155px;background:linear-gradient(160deg,#8a7c62,#6b5a43)" role="img" aria-label="Aerial photo of earthmoving equipment on site"></div>
<div class="ph" style="left:876px;top:1942px;width:168px;height:155px;background:linear-gradient(160deg,#6a4a30,#a89a86)" role="img" aria-label="Photo of concrete drainage structure in trench"></div>
<div class="ph" style="left:701px;top:2105px;width:168px;height:155px;background:linear-gradient(160deg,#7a8a7a,#4f7a5a)" role="img" aria-label="Aerial photo of a pond and landscaped development"></div>
<div class="ph" style="left:876px;top:2105px;width:168px;height:155px;background:linear-gradient(160deg,#9a9a8a,#b0a040)" role="img" aria-label="Photo of a yellow wheel loader moving soil"></div>
<div class="ph" style="left:701px;top:2269px;width:168px;height:154px;background:linear-gradient(180deg,#4f6a3a,#8a8a84)" role="img" aria-label="Photo of plant equipment and curbing"></div>
<div class="ph" style="left:876px;top:2269px;width:168px;height:154px;background:linear-gradient(180deg,#5c86c8,#c89a30 60%,#4a5a3a)" role="img" aria-label="Photo of a long-reach excavator beside a channel"></div>

<!-- Call to action -->
<div class="abs cta" role="img" aria-label="Darkened photo of heavy machinery silhouettes"></div>
<h2 class="abs cta-title">Nemo enim ipsam voluptatem<br>quia voluptas sit asperts</h2>
<p class="abs cta-sub">Lorem ipsum dolor sit amet, consectetur</p>
<a class="abs btn btn-outline" style="left:523px;top:2712px;width:155px;height:45px">Contact Us <span class="arrow"><svg width="16" height="10" viewBox="0 0 16 10"><path d="M1 5h13M10 1l4 4-4 4" stroke="#fff" stroke-width="2" fill="none"/></svg></span></a>

<!-- Footer -->
<svg class="abs" style="left:0;top:2815px" width="1200" height="423" viewBox="0 0 1200 423">
  <polygon points="0,82 600,0 1200,82 1200,423 0,423" fill="#8a8a8c"/>
  <polygon points="0,98 600,16 1200,98 1200,423 0,423" fill="#f4f3f6"/>
</svg>
<div class="abs brand" style="top:2968px">
  <div class="brand-mark" style="width:42px;height:42px"></div>
  <div class="brand-name" style="font-size:19px">HARLOW STONEFIELD<small style="font-size:11px">CIVIL CONSTRUCTION</small></div>
</div>
<p class="abs foot-about">Sed ut perspiciatis unde omnis iste natusauror sit voluptatem accusantium doloremque laudan tium, satur delor daytra lormutes.</p>

<div class="abs" style="left:493px;top:2941px">
  <h3 class="foot-h">Contact us</h3>
  <ul class="foot-list" style="margin-top:14px">
    <li style="line-height:24px"><svg class="ico" viewBox="0 0 14 14"><path d="M7 13S2 7.5 2 5a5 5 0 0 1 10 0c0 2.5-5 8-5 8z" fill="#222"/><circle cx="7" cy="5" r="1.8" fill="#f4f3f6"/></svg><span>Harlow Stonefield,<br>Lorem Ipsum Is Simple</span></li>
    <li style="margin-top:14px"><svg class="ico" viewBox="0 0 14 14"><path d="M3 1l3 3-1.5 2a8 8 0 0 0 3.5 3.5L10 8l3 3-2 2C6 13 1 8 1 3z" fill="#222"/></svg><span>+1 555 010 2040</span></li>
    <li style="margin-top:18px"><svg class="ico" viewBox="0 0 14 14"><rect x="1" y="3" width="12" height="9" fill="#222"/><path d="M1 3l6 5 6-5" stroke="#f4f3f6" fill="none"/></svg><span>info@harlowstonefield.com</span></li>
  </ul>
</div>

<div class="abs" style="left:718px;top:2940px">
  <h3 class="foot-h">Menu</h3>
  <ul class="foot-list" style="margin-top:8px;line-height:28px">
    <li><span>»</span>Home</li><li><span>»</span>About us</li><li><span>»</span>Project Gallery</li><li><span>»</span>Employee Application</li><li><span>»</span>Contact us</li>
  </ul>
</div>

<div class="abs" style="left:921px;top:2941px">
  <h3 class="foot-h">Connect With Us</h3>
  <ul class="foot-list" style="margin-top:10px">
    <li><span class="soc-dot"></span>Newsfeed</li>
    <li style="margin-top:20px"><span class="soc-dot"></span>Updates</li>
    <li style="margin-top:20px"><span class="soc-dot"></span>Network</li>
  </ul>
</div>

<div class="abs foot-rule"></div>
<p class="abs copy">Copyrights @ 2019 All Rights Reserved</p>

</body>
</html>
```